Brindlow Electrical Solutions needs a website

We need a new website designed because our current one is outdated. I would like a one-page website. We are a B2B company and want to maintain a professional appearance to appeal to project managers and directors.

for some reference, these are a few of my competitor's websites; we offer the same services.

https://valtorwiring.com.au/services
https://www.dunsary.com.au/mechanical-electrical-services/
https://www.gravik.com.au/

Industry/Entity Type

Electrical

Number of Pages Required

1 page

Font styles to use
Sans Serif

Colors
0054AA
0677BA
7BADD7
CADEEF
E8F1F8

```html
<!DOCTYPE html>
<html lang="en">
<head>
<meta charset="utf-8">
<title>Brindlow Electrical Solutions</title>
<link href="https://fonts.googleapis.com/css2?family=Montserrat:wght@400;500;600;700;800&display=swap" rel="stylesheet">
<style>
:root{
  --cyan:#17b7e8;
  --cyan-dark:#0d9fd0;
  --navy:#0054aa;
  --blue:#0677ba;
  --sky:#7badd7;
  --pale:#cadeef;
  --mist:#e8f1f8;
  --ink:#1d2430;
  --grey:#f1f3f5;
  --text:#5b6470;
  --footer:#121417;
  --white:#ffffff;
}
*{box-sizing:border-box;margin:0;padding:0}
html,body{width:1200px;height:2380px;overflow:hidden}
body{font-family:"Montserrat",Arial,sans-serif;color:var(--ink);background:var(--white);position:relative}
section,header,footer{overflow:hidden}
.container{width:860px;margin:0 auto;position:relative}

/* top bar */
.topbar{height:34px;background:var(--cyan);color:var(--white);font-size:11px;font-weight:500}
.topbar .container{display:flex;justify-content:flex-end;align-items:center;height:34px;gap:26px}
.topbar span{display:flex;align-items:center;gap:6px}

/* header */
.site-header{height:70px;background:var(--white);border-bottom:1px solid #e4e8ec}
.site-header .container{display:flex;align-items:center;justify-content:space-between;height:69px}
.brand{display:flex;align-items:center;gap:8px;font-size:15px;font-weight:800;color:var(--navy);letter-spacing:.3px}
.brand-mark{width:14px;height:14px;background:var(--cyan)}
.main-nav{display:flex;align-items:center;gap:6px;font-size:12px;font-weight:600}
.main-nav a{color:var(--ink);text-decoration:none;padding:7px 14px;border-radius:3px}
.main-nav a.active{background:var(--cyan);color:var(--white)}
.nav-icons{display:flex;gap:12px;margin-left:14px}

/* hero */
.hero{height:256px;position:relative;background:linear-gradient(90deg,#dfe3e6 0%,#f5f6f7 45%,#ffffff 70%)}
.hero-image{position:absolute;left:0;top:0;width:620px;height:256px;background:radial-gradient(ellipse at 50% 45%,#ffffff 0%,#e7ebee 45%,#c9d0d5 100%)}
.hero-copy{position:absolute;left:640px;top:52px;width:380px}
.hero-kicker{font-size:11px;color:var(--text);margin-bottom:6px}
.hero-title{font-size:30px;font-weight:800;line-height:1.12;color:var(--ink)}
.hero-title em{font-style:normal;color:var(--cyan)}
.btn-outline{display:inline-block;margin-top:18px;border:2px solid var(--cyan);color:var(--cyan);font-size:10px;font-weight:700;letter-spacing:1px;padding:8px 20px;border-radius:20px}

/* intro band */
.intro{height:160px;background:var(--cyan);display:flex;align-items:center}
.intro p{width:860px;margin:0 auto;text-align:center;color:var(--white);font-size:19px;font-weight:700;line-height:1.45}
.intro p span{font-weight:500}

/* news */
.news{padding:36px 0 20px;height:500px}
.section-title{text-align:center;font-size:26px;font-weight:700;color:var(--ink)}
.section-title::after{content:"";display:block;width:44px;height:3px;background:var(--cyan);margin:10px auto 0}
.news-grid{display:grid;grid-template-columns:repeat(4,1fr);grid-template-rows:180px 180px;gap:8px;margin-top:28px}
.news-tile{position:relative;overflow:hidden}
.news-tile.wide{grid-column:span 2}
.news-photo{position:absolute;inset:0}
.photo-worker{background:linear-gradient(160deg,#9fb8c9 0%,#e98a3a 60%,#c8662a 100%)}
.photo-event{background:linear-gradient(160deg,#a9c3d6 0%,#7b8fa0 55%,#e58b3b 100%)}
.photo-wind{background:linear-gradient(180deg,#cfe3f2 0%,#9cc3e0 60%,#4f87b6 100%)}
.news-caption{position:absolute;left:0;right:0;bottom:0;background:rgba(23,183,232,.88);color:var(--white);padding:8px 10px}
.news-caption small{display:block;font-size:9px;opacity:.9}
.news-caption strong{display:block;font-size:12px;font-weight:700;margin-top:2px}

/* features */
.features{height:310px;background:var(--grey);padding-top:48px}
.feature-list{display:grid;grid-template-columns:repeat(4,1fr);gap:30px;text-align:center}
.feature-icon{width:58px;height:58px;border-radius:50%;background:var(--cyan);margin:0 auto 14px;display:flex;align-items:center;justify-content:center}
.feature h3{font-size:14px;font-weight:700;margin-bottom:8px}
.feature p{font-size:10.5px;line-height:1.55;color:var(--text)}
.btn-small{display:inline-block;margin-top:12px;background:var(--cyan);color:var(--white);font-size:9px;font-weight:600;padding:5px 14px;border-radius:12px}

/* services */
.services{height:360px;padding-top:34px}
.service-list{display:grid;grid-template-columns:repeat(4,1fr);gap:14px;margin-top:28px}
.service-photo{height:180px}
.photo-building{background:linear-gradient(180deg,#b8cad8 0%,#5b6d80 100%)}
.photo-handshake{background:linear-gradient(135deg,#d4dde6 0%,#8fa2b3 100%)}
.photo-maintenance{background:linear-gradient(160deg,#f09a45 0%,#d96a22 100%)}
.photo-meter{background:linear-gradient(160deg,#e6e8ea 0%,#a9afb5 100%)}
.service h3{text-align:center;font-size:13px;font-weight:700;margin-top:12px}
.rating{display:flex;justify-content:center;gap:3px;margin-top:6px}

/* accreditations */
.accreditations{height:430px;position:relative;padding-top:36px}
.accred-bg{position:absolute;inset:0;background:linear-gradient(180deg,rgba(23,183,232,.92) 0%,rgba(13,159,208,.9) 100%),linear-gradient(90deg,#5a7e98,#2f4f6c)}
.accreditations .container{position:relative}
.accreditations .section-title{color:var(--white);line-height:1.2}
.accreditations .section-title::after{background:var(--white)}
.badge-grid{display:grid;grid-template-columns:repeat(6,48px);gap:16px 64px;justify-content:center;margin-top:28px}
.badge{width:48px;height:48px;border-radius:50%;background:rgba(255,255,255,.85)}
.badge.square{border-radius:6px;background:rgba(255,255,255,.7)}

/* footer */
.site-footer{height:260px;background:var(--footer);color:#c9ced4}
.footer-top{display:flex;justify-content:space-between;padding-top:26px}
.footer-brand .brand{color:var(--white)}
.footer-brand h4{color:var(--white);font-size:12px;font-weight:700;margin:14px 0 6px}
.footer-brand p{font-size:10.5px;line-height:1.6}
.social{display:flex;gap:8px;margin-top:10px}
.social i{width:16px;height:16px;border-radius:50%;background:var(--cyan);display:block}
.footer-quote{width:470px;font-size:12.5px;line-height:1.6;color:#e3e6ea;padding-top:8px}
.footer-nav{display:flex;justify-content:center;gap:28px;font-size:11px;margin-top:18px}
.copyright{text-align:center;font-size:10px;color:#838a92;margin-top:12px;border-top:1px solid #2a2e33;padding-top:10px}
</style>
</head>
<body>

<div class="topbar">
  <div class="container">
    <span><svg width="11" height="11" viewBox="0 0 24 24"><path d="M6.6 10.8a15 15 0 006.6 6.6l2.2-2.2c.3-.3.7-.4 1-.2 1.1.4 2.3.6 3.6.6.6 0 1 .4 1 1V20c0 .6-.4 1-1 1A17 17 0 013 4c0-.6.4-1 1-1h3.5c.6 0 1 .4 1 1 0 1.3.2 2.5.6 3.6.1.3 0 .7-.2 1z" fill="#fff"/></svg>1300 482 915</span>
    <span>Language: English</span>
    <span>Client Login</span>
  </div>
</div>

<header class="site-header">
  <div class="container">
    <div class="brand"><span class="brand-mark"></span>Brindlow Electrical Solutions</div>
    <nav class="main-nav">
      <a class="active">Home</a><a>About</a><a>Projects</a><a>Careers</a><a>Contact</a>
      <div class="nav-icons">
        <svg width="13" height="13" viewBox="0 0 24 24"><circle cx="10" cy="10" r="6.5" fill="none" stroke="#1d2430" stroke-width="2.5"/><path d="M15 15l6 6" stroke="#1d2430" stroke-width="2.5"/></svg>
        <svg width="13" height="13" viewBox="0 0 24 24"><path d="M3 6h18M3 12h18M3 18h18" stroke="#1d2430" stroke-width="2.5"/></svg>
      </div>
    </nav>
  </div>
</header>

<section class="hero">
  <div class="hero-image" role="img" aria-label="Light bulb with visible wiring beside electrician's screwdrivers and pliers"></div>
  <div class="hero-copy">
    <p class="hero-kicker">Nationwide Australian Commercial Service</p>
    <h1 class="hero-title">Strong <em>Commercial</em><br>Electrical Expertise</h1>
    <span class="btn-outline">VIEW OUR SERVICES</span>
  </div>
</section>

<section class="intro">
  <p>Brindlow specialise in Commercial Electrical Installations, Service and Maintenance for a broad range of clients in the private and public sectors. <span>More Info</span></p>
</section>

<section class="news">
  <div class="container">
    <h2 class="section-title">News</h2>
    <div class="news-grid">
      <article class="news-tile">
        <div class="news-photo photo-worker" role="img" aria-label="Electrician in hi-vis orange workwear on site"></div>
        <div class="news-caption"><small>March 2019</small><strong>Congratulations Stephen</strong></div>
      </article>
      <article class="news-tile">
        <div class="news-photo photo-event" role="img" aria-label="Staff gathered outdoors for an environment day event"></div>
        <div class="news-caption"><small>June 2019</small><strong>World Environment Day</strong></div>
      </article>
      <article class="news-tile">
        <div class="news-photo photo-event" role="img" aria-label="Team planting trees for an environment day"></div>
        <div class="news-caption"><small>June 2018</small><strong>World Environment Day</strong></div>
      </article>
      <article class="news-tile">
        <div class="news-photo photo-worker" role="img" aria-label="Apprentice electrician in safety gear"></div>
        <div class="news-caption"><small>May 2019</small><strong>New Apprentice Intake</strong></div>
      </article>
      <article class="news-tile">
        <div class="news-photo photo-worker" role="img" aria-label="Electrician smiling in orange workwear"></div>
        <div class="news-caption"><small>April 2019</small><strong>Congratulations Daniel</strong></div>
      </article>
      <article class="news-tile wide">
        <div class="news-photo photo-wind" role="img" aria-label="Row of wind turbines on a coastal plain under blue sky"></div>
        <div class="news-caption"><small>February 2019</small><strong>Power Generation Project Awarded</strong></div>
      </article>
      <article class="news-tile">
        <div class="news-photo photo-worker" role="img" aria-label="Site supervisor in hi-vis uniform"></div>
        <div class="news-caption"><small>January 2019</small><strong>Congratulations Mark</strong></div>
      </article>
    </div>
  </div>
</section>

<section class="features">
  <div class="container feature-list">
    <div class="feature">
      <div class="feature-icon"><svg width="26" height="26" viewBox="0 0 24 24"><path d="M12 2l3 6.5 7 .8-5.2 4.8 1.4 7L12 17.6 5.8 21l1.4-7L2 9.3l7-.8z" fill="#fff"/></svg></div>
      <h3>Quality</h3>
      <p>Skilled licensed tradespeople deliver safe, compliant work to every commercial site we service.</p>
      <span class="btn-small">Read More</span>
    </div>
    <div class="feature">
      <div class="feature-icon"><svg width="26" height="26" viewBox="0 0 24 24"><circle cx="12" cy="12" r="9" fill="none" stroke="#fff" stroke-width="2.2"/><path d="M12 7v5l3.5 2.5" stroke="#fff" stroke-width="2.2" fill="none"/></svg></div>
      <h3>Timely Delivery</h3>
      <p>Our project teams plan ahead so works finish on schedule with minimal disruption to you.</p>
      <span class="btn-small">Read More</span>
    </div>
    <div class="feature">
      <div class="feature-icon"><svg width="26" height="26" viewBox="0 0 24 24"><path d="M5 19C5 9 11 5 20 4c0 9-4 15-13 15" fill="#fff"/><path d="M4 21l9-9" stroke="#17b7e8" stroke-width="1.6"/></svg></div>
      <h3>Eco-Minded</h3>
      <p>We recommend efficient lighting and energy solutions that cut running costs and emissions.</p>
      <span class="btn-small">Read More</span>
    </div>
    <div class="feature">
      <div class="feature-icon"><svg width="26" height="26" viewBox="0 0 24 24"><path d="M5 12.5l4.5 4.5L19 7.5" fill="none" stroke="#fff" stroke-width="2.8"/></svg></div>
      <h3>Money Back Guaranteed</h3>
      <p>If our workmanship falls short, we will make it right or refund the affected work.</p>
      <span class="btn-small">Read More</span>
    </div>
  </div>
</section>

<section class="services">
  <div class="container">
    <h2 class="section-title">Electrical Services</h2>
    <div class="service-list">
      <div class="service">
        <div class="service-photo photo-building" role="img" aria-label="Modern commercial office building exterior"></div>
        <h3>Partners &amp; Projects</h3>
        <div class="rating"><svg width="60" height="8" viewBox="0 0 60 8"><g fill="#17b7e8"><circle cx="4" cy="4" r="3"/><circle cx="16" cy="4" r="3"/><circle cx="28" cy="4" r="3"/><circle cx="40" cy="4" r="3"/><circle cx="52" cy="4" r="3"/></g></svg></div>
      </div>
      <div class="service">
        <div class="service-photo photo-handshake" role="img" aria-label="Business handshake sealing a service agreement"></div>
        <h3>Service Agreements</h3>
        <div class="rating"><svg width="60" height="8" viewBox="0 0 60 8"><g fill="#17b7e8"><circle cx="4" cy="4" r="3"/><circle cx="16" cy="4" r="3"/><circle cx="28" cy="4" r="3"/><circle cx="40" cy="4" r="3"/><circle cx="52" cy="4" r="3"/></g></svg></div>
      </div>
      <div class="service">
        <div class="service-photo photo-maintenance" role="img" aria-label="Technician in orange hi-vis performing maintenance"></div>
        <h3>Preventative Maintenance</h3>
        <div class="rating"><svg width="60" height="8" viewBox="0 0 60 8"><g fill="#17b7e8"><circle cx="4" cy="4" r="3"/><circle cx="16" cy="4" r="3"/><circle cx="28" cy="4" r="3"/><circle cx="40" cy="4" r="3"/><circle cx="52" cy="4" r="3"/></g></svg></div>
      </div>
      <div class="service">
        <div class="service-photo photo-meter" role="img" aria-label="Close-up of a digital electricity meter display"></div>
        <h3>Advanced Metering</h3>
        <div class="rating"><svg width="60" height="8" viewBox="0 0 60 8"><g fill="#17b7e8"><circle cx="4" cy="4" r="3"/><circle cx="16" cy="4" r="3"/><circle cx="28" cy="4" r="3"/><circle cx="40" cy="4" r="3"/><circle cx="52" cy="4" r="3"/></g></svg></div>
      </div>
    </div>
  </div>
</section>

<section class="accreditations">
  <div class="accred-bg" role="img" aria-label="Office tower photo under a cyan tint"></div>
  <div class="container">
    <h2 class="section-title">Accreditations &amp;<br>Associations</h2>
    <div class="badge-grid">
      <div class="badge square"></div><div class="badge"></div><div class="badge square"></div><div class="badge"></div><div class="badge square"></div><div class="badge"></div>
      <div class="badge"></div><div class="badge square"></div><div class="badge"></div><div class="badge"></div><div class="badge square"></div><div class="badge"></div>
      <div class="badge"></div><div class="badge"></div><div class="badge"></div><div class="badge square"></div><div class="badge"></div><div class="badge"></div>
      <div class="badge"></div><div class="badge square"></div><div class="badge"></div><div class="badge"></div><div class="badge"></div><div class="badge square"></div>
    </div>
  </div>
</section>

<footer class="site-footer">
  <div class="container">
    <div class="footer-top">
      <div class="footer-brand">
        <div class="brand"><span class="brand-mark"></span>Brindlow Electrical Solutions</div>
        <h4>Brindlow Head Office</h4>
        <p>14 Harlow Street<br>Merivale QLD 4101<br>Phone 1300 482 915</p>
        <div class="social"><i></i><i></i><i></i></div>
      </div>
      <p class="footer-quote">"Throughout our proud history we have expanded our services to meet the needs of a diverse range of clients in both the commercial and industrial sectors."</p>
    </div>
    <nav class="footer-nav"><span>Home</span><span>About</span><span>Projects</span><span>Careers</span><span>Contact</span></nav>
    <p class="copyright">© Brindlow all rights reserved. Brindlow Electrical Services &amp; Associates</p>
  </div>
</footer>

</body>
</html>
```